Tallow Crest Software PowerPoint template

We are a software company selling endpoint visibility, access and security technology to enterprise-level IT departments.
Our technology helps organizations gain comprehensive visibility into and control over devices accessing their corporate network so they can quickly identify and address suspicious activity on the network that could lead to potential threats like data breaches.
This technology can cost organizations upwards of $1M - depending on the size of the organization. Our primary clients are Meridane 2,000 companies.
We want a professional, polished PowerPoint template that we can use for all company presentations. Please include:
Title page
Section page
General info page
Thank you page
Logo options and color specs are attached.
Please include our tagline on at least the title page: Discover the edge. Optimize the whole.

```html
<!DOCTYPE html>
<html lang="en">
<head>
<meta charset="utf-8">
<title>Tallow Crest Software – General Info Slide</title>
<link rel="stylesheet" href="https://fonts.googleapis.com/css2?family=Roboto+Condensed:wght@400;700&family=Questrial&display=swap">
<style>
  :root {
    --brand-red: #b3181f;
    --brand-orange: #e3804f;
    --footer-orange: #e07f52;
    --rule-grey: #d9d9d9;
    --body-ink: #333333;
    --paper: #ffffff;
  }
  * { margin: 0; padding: 0; box-sizing: border-box; }
  html, body { width: 1200px; height: 900px; overflow: hidden; background: var(--paper); }
  .slide { position: relative; width: 1200px; height: 900px; background: var(--paper); }

  .slide-header {
    position: absolute; left: 0; top: 0; width: 1200px; height: 80px;
    border-bottom: 1.5px solid var(--rule-grey);
  }
  .project-title {
    position: absolute; left: 26px; top: 22px;
    font-family: "Roboto Condensed", "Arial Narrow", sans-serif;
    font-weight: 700; font-size: 46px; line-height: 1; letter-spacing: -0.5px;
    color: var(--brand-red);
  }
  .project-title .accent { color: var(--brand-orange); }

  .brand {
    position: absolute; right: 24px; top: 14px;
    display: flex; align-items: center; gap: 14px;
  }
  .brand-mark { width: 30px; height: 30px; background: var(--brand-orange); }
  .brand-name {
    font-family: "Roboto Condensed", "Arial Narrow", sans-serif;
    font-weight: 700; font-size: 22px; line-height: 24px; letter-spacing: 4px;
    color: var(--brand-red); text-transform: uppercase;
  }

  .info-section { position: absolute; left: 61px; width: 1040px; }
  .info-section:nth-of-type(1) { top: 142px; }
  .info-section:nth-of-type(2) { top: 384px; }
  .info-section:nth-of-type(3) { top: 598px; }
  .info-subtitle {
    font-family: "Roboto Condensed", Arial, sans-serif;
    font-weight: 700; font-size: 26px; line-height: 30px;
    color: var(--brand-orange);
  }
  .info-body {
    margin-top: 13px;
    font-family: "Questrial", "Century Gothic", sans-serif;
    font-size: 20.3px; line-height: 30px; color: var(--body-ink);
  }

  .slide-footer {
    position: absolute; left: 0; bottom: 0; width: 1200px; height: 42px;
    background: var(--footer-orange); color: #fff;
    font-family: "Roboto Condensed", "Arial Narrow", sans-serif; font-size: 18px;
    display: flex; align-items: center; justify-content: space-between;
    padding: 0 12px 0 12px;
  }
</style>
</head>
<body>
<main class="slide">
  <header class="slide-header">
    <h1 class="project-title">PROJECT <span class="accent">TITLE HERE</span></h1>
    <div class="brand">
      <span class="brand-mark"></span>
      <span class="brand-name">Tallow Crest<br>Software</span>
    </div>
  </header>

  <section class="info-section">
    <h2 class="info-subtitle">Subtitle Here</h2>
    <p class="info-body">Odio possim splendide sea cu. Qui nibh mazim insolens ei, tritani suscipit petentium vis ut. His ex reque dissentiet. Mel vocent numquam et, cetero vocent abhorreant cum ut, sit dictas vivendum eu. Ei eos officiis eleifend expetenda, per ei adhuc decore euismod, quando equidem mei an. Novum adipiscing mea ad, soluta ponderum urbanitas nec ea.</p>
  </section>

  <section class="info-section">
    <h2 class="info-subtitle">Subtitle Here</h2>
    <p class="info-body">Odio possim splendide sea cu. Qui nibh mazim insolens ei, tritani suscipit petentium vis ut. His ex reque dissentiet. Mel vocent numquam et, cetero vocent abhorreant cum ut, sit dictas vivendum eu. Ei eos officiis eleifend expetenda, per ei adhuc decore euismod, quando equidem mei an. Novum adipiscing mea ad, soluta ponderum urbanitas nec ea.</p>
  </section>

  <section class="info-section">
    <h2 class="info-subtitle">Subtitle Here</h2>
    <p class="info-body">Odio possim splendide sea cu. Qui nibh mazim insolens ei, tritani suscipit petentium vis ut. His ex reque dissentiet. Mel vocent numquam et, cetero vocent abhorreant cum ut, sit dictas vivendum eu. Ei eos officiis eleifend expetenda, per ei adhuc decore euismod, quando equidem mei an. Novum adipiscing mea ad, soluta ponderum urbanitas nec ea.</p>
  </section>

  <footer class="slide-footer">
    <span class="copyright">COPYRIGHT TEXT HERE</span>
    <span class="page-number">Page : 01</span>
  </footer>
</main>
</body>
</html>
```